Inviting A6 Flyer for Church membership

We need an A6 size flyer for the church. We are looking for something fresh, inviting and impactful. Church new logo and current flyer design attached.
Back text as follows:
We would love to have you join us as our SPECIAL GUEST this Sunday at 10am.
You can find us at Harvest Gateway Family Church, 17-19 Meadowbrook Lane
(Behind Farley), Pellham Brook Village,KL7 2RT
For more information or for a chat, please call us on 07614 290457 / 07781 504316 or email church@hgfcuk.org
Target Market(s)
Church
Industry/Entity Type
Church
Colors
Designer to choose colors to be used in the design.
Requirements
Must have
- fresh, inviting and impactful.
- Chruch logo (attached)
Should not have
- Too much going on

```html
<!DOCTYPE html>
<html lang="en">
<head>
<meta charset="utf-8">
<title>Harvest Gateway Family Church – Invitation Flyer</title>
<link rel="stylesheet" href="https://fonts.googleapis.com/css2?family=Didact+Gothic&family=Roboto+Condensed:wght@300;400&display=swap">
<style>
  :root {
    --page: #e9e8e6;
    --paper-light: #fbf6ea;
    --paper-mid: #f1e4c6;
    --paper-deep: #e3c993;
    --red: #c8202f;
    --ink: #2b2b2b;
    --brand-blue: #1f6fb0;
    --white: #ffffff;
  }
  * { box-sizing: border-box; margin: 0; padding: 0; }
  html, body { width: 860px; height: 1200px; overflow: hidden; }
  body { background: var(--page); position: relative; font-family: "Didact Gothic", sans-serif; color: var(--ink); }

  .card {
    position: absolute; left: 40px; width: 780px; height: 552px; overflow: hidden;
    background: linear-gradient(180deg, var(--paper-light) 0%, var(--paper-mid) 60%, var(--paper-deep) 100%);
    box-shadow: 0 4px 14px rgba(0,0,0,0.25);
  }
  .card--front { top: 34px; }
  .card--back { top: 626px; }

  /* Front */
  .front-photo { position: absolute; inset: 0; }
  .brand { position: absolute; left: 40px; top: 34px; width: 270px; text-align: center; }
  .brand-mark { width: 70px; height: 70px; border-radius: 50%; background: var(--brand-blue); margin: 0 auto 14px; }
  .brand-name { font-family: "Roboto Condensed", sans-serif; font-weight: 400; color: var(--red); font-size: 21px; letter-spacing: 1px; line-height: 1.05; text-transform: uppercase; }
  .headline { position: absolute; left: 36px; top: 212px; font-family: "Roboto Condensed", sans-serif; font-weight: 300; color: var(--red); font-size: 66px; line-height: 74px; letter-spacing: 1px; }
  .headline-rule { position: absolute; left: 39px; top: 360px; width: 246px; height: 3px; background: var(--red); }
  .headline-rule::after { content: ""; position: absolute; right: -2px; top: -2px; width: 7px; height: 7px; border-radius: 50%; background: var(--red); }
  .invite-lead { position: absolute; left: 42px; top: 402px; font-size: 21px; line-height: 27px; }
  .address { position: absolute; left: 46px; top: 505px; display: flex; gap: 8px; font-family: "Roboto Condensed", sans-serif; font-size: 13px; line-height: 18px; }
  .pin { flex: none; width: 12px; height: 17px; margin-top: 1px; }

  /* Back */
  .back-photo { position: absolute; left: 0; top: 0; width: 780px; height: 330px; }
  .back-message { position: absolute; left: 0; right: 0; top: 356px; text-align: center; font-size: 19px; line-height: 24px; }
  .contact-band { position: absolute; left: 0; right: 0; top: 458px; height: 37px; background: var(--red); color: var(--white); font-family: "Roboto Condensed", sans-serif; font-size: 15.5px; line-height: 37px; text-align: center; }
  .back-address { position: absolute; left: 0; right: 0; top: 510px; display: flex; justify-content: center; align-items: center; gap: 9px; font-family: "Roboto Condensed", sans-serif; font-size: 15.5px; }
</style>
</head>
<body>

<section class="card card--front">
  <svg class="front-photo" width="780" height="552" viewBox="0 0 780 552">
    <defs>
      <linearGradient id="familyTones" x1="0" y1="0" x2="1" y2="1">
        <stop offset="0" stop-color="#e8d2b4"/>
        <stop offset="0.45" stop-color="#a46c4e"/>
        <stop offset="1" stop-color="#6d86a8"/>
      </linearGradient>
    </defs>
    <path d="M432 0 C 330 140, 320 390, 441 552 L780 552 L780 0 Z" fill="url(#familyTones)" role="img" aria-label="Photo of a smiling family of four outdoors"/>
    <path d="M432 0 C 330 140, 320 390, 441 552" fill="none" stroke="var(--white)" stroke-width="7"/>
  </svg>

  <div class="brand">
    <div class="brand-mark"></div>
    <div class="brand-name">Harvest Gateway<br>Ministries</div>
  </div>

  <h1 class="headline">YOU’RE<br>INVITED!</h1>
  <div class="headline-rule"></div>

  <p class="invite-lead">Join us as our<br>SPECIAL GUEST<br>this Sunday at 10am</p>

  <div class="address">
    <svg class="pin" viewBox="0 0 12 17"><path d="M6 0C2.7 0 0 2.6 0 5.9 0 10.3 6 17 6 17s6-6.7 6-11.1C12 2.6 9.3 0 6 0zm0 8.3A2.4 2.4 0 1 1 6 3.5a2.4 2.4 0 0 1 0 4.8z" fill="var(--red)"/></svg>
    <p>Harvest Gateway Family Church, 17-19 Meadowbrook Lane<br>(Behind Farley), Pellham Brook Village,KL7 2RT</p>
  </div>
</section>

<section class="card card--back">
  <svg class="back-photo" width="780" height="330" viewBox="0 0 780 330">
    <defs>
      <linearGradient id="cityTones" x1="0" y1="0" x2="0" y2="1">
        <stop offset="0" stop-color="#c99a8a"/>
        <stop offset="0.5" stop-color="#8a6a5c"/>
        <stop offset="1" stop-color="#3c3530"/>
      </linearGradient>
    </defs>
    <path d="M0 0 H780 V275 Q390 350 0 275 Z" fill="url(#cityTones)" role="img" aria-label="Photo of a city river skyline with a lit bridge at dusk"/>
    <path d="M0 275 Q390 350 780 275" fill="none" stroke="var(--white)" stroke-width="8"/>
  </svg>

  <p class="back-message">We would love to have you join us as our SPECIAL GUEST this Sunday at 10am.<br>You can find us at Harvest Gateway Family Church, 17-19 Meadowbrook Lane<br>(Behind Farley), Pellham Brook Village,KL7 2RT</p>

  <div class="contact-band">For more information or for a chat, please call us on 07614 290457 / 07781 504316 or email church@hgfcuk.org</div>

  <div class="back-address">
    <svg class="pin" viewBox="0 0 12 17"><path d="M6 0C2.7 0 0 2.6 0 5.9 0 10.3 6 17 6 17s6-6.7 6-11.1C12 2.6 9.3 0 6 0zm0 8.3A2.4 2.4 0 1 1 6 3.5a2.4 2.4 0 0 1 0 4.8z" fill="var(--red)"/></svg>
    <p>Harvest Gateway Family Church, 17-19 Meadowbrook Lane (Behind Farley), Pellham Brook Village,KL7 2RT</p>
  </div>
</section>

</body>
</html>
```